依頼詳細
当院がこの度4月より、木曜診療・駐車場提携・CT導入をしたため、そのお知らせのチラシを作成いただきたいです。(A4裏表)
ラフ・素材等はございます。HP(http://mk-dental.net/)取っていただいても構いません。

※発送はポミネオ様で行う予定です。(https://pomineo.com/directmail/large-sized-postcard/
※まず表面案だけで構いませんのでお出しいただけますと幸いです。その後当選の方が決まり次第裏面もお願いしようと思います。
記載項目
添付ラフ通り
サイズ
A4
ページ数
両面
希望イメージ
シンプル 複雑
単色 カラフル
暗い 明るい
日常 高級
遊び心 厳粛
未来的 伝統的
女性的 男性的
希望する色
緑系
納品ファイル
• イラストレーター形式 (.ai)
• PNG形式 (.png)
補足説明
ポミネオのDM(https://pomineo.com/directmail/large-sized-postcard/)で患者様に発送するため、ポミネオの規定で作成願えますでしょうか。
■ 選んだ理由

全体的なデザインバランスが良かったため

■ 提案者全員のお礼・コメント

この度はご参加いただきまして誠に有難うございました!
今後とも宜しくお願いいたします。

```html
<!DOCTYPE html>
<html lang="ja">
<head>
<meta charset="utf-8">
<title>桜川ファミリー歯科 からのご案内</title>
<link rel="stylesheet" href="https://fonts.googleapis.com/css2?family=M+PLUS+Rounded+1c:wght@500;700;800&family=Noto+Sans+JP:wght@400;500;700&display=swap">
<style>
:root{
  --green:#3aa55a;
  --green-dark:#2b8a45;
  --green-pale:#9fd2a8;
  --map-fill:#7cbb84;
  --ink:#333;
  --grey:#888;
  --line:#bbb;
  --water-top:#ffffff;
  --water-bottom:#cfe6f1;
}
*{margin:0;padding:0;box-sizing:border-box}
html,body{width:849px;height:1200px;overflow:hidden;background:#fff}
body{font-family:"Noto Sans JP",sans-serif;color:var(--ink);position:relative}
.round{font-family:"M PLUS Rounded 1c",sans-serif}

.header{position:absolute;left:60px;top:24px;display:flex;align-items:flex-end;gap:14px}
.brand{display:flex;align-items:center;gap:8px}
.brand-dot{width:34px;height:34px;border-radius:50%;background:var(--green)}
.brand-name{font-family:"M PLUS Rounded 1c",sans-serif;font-weight:800;color:var(--green);font-size:34px;line-height:1}
.brand-en{font-family:"M PLUS Rounded 1c",sans-serif;font-weight:700;color:var(--green);font-size:10px;letter-spacing:1px;margin-left:42px;margin-top:2px}
.header-sub{font-size:20px;font-weight:500;padding-bottom:16px}
.rule{position:absolute;left:60px;right:60px;height:2px;background:var(--green)}

.headline{position:absolute;top:120px;left:0;right:0;text-align:center;font-family:"M PLUS Rounded 1c",sans-serif;font-weight:700;font-size:30px;color:var(--green)}
.headline .dark{color:var(--ink)}
.headline .big{font-size:40px;color:var(--ink)}

.sched{position:absolute;font-size:9px}
.sched-cap{margin-bottom:4px}
.sched table{border-collapse:collapse}
.sched td,.sched th{border:1px solid var(--line);text-align:center;font-weight:500}
.sched th{font-weight:700}
.sched .dot{color:var(--ink)}
.sched .new{color:var(--green)}
.sched-note{margin-top:4px}
.sched.old{left:55px;top:196px}
.sched.old td,.sched.old th{width:26px;height:26px}
.sched.old td.time,.sched.old th.time{width:72px}
.sched.nowx{left:420px;top:190px;font-size:11px}
.sched.nowx td,.sched.nowx th{width:38px;height:40px}
.sched.nowx td.time,.sched.nowx th.time{width:112px}
.arrow{position:absolute;left:355px;top:216px}

.parking-title{position:absolute;top:370px;left:0;right:0;text-align:center;font-family:"M PLUS Rounded 1c",sans-serif;font-weight:700;color:var(--green);font-size:34px}
.parking-title .p{display:inline-block;width:34px;height:34px;background:var(--green);color:#fff;font-size:26px;line-height:34px;border-radius:4px;margin-right:14px;vertical-align:4px}
.parking-title small{font-size:20px}
.badge{position:absolute;left:602px;top:350px;width:58px;height:58px;border-radius:50%;border:2px solid var(--green);color:var(--green);font-size:9px;font-weight:700;display:flex;align-items:center;justify-content:center;text-align:center;line-height:1.3;transform:rotate(-10deg)}
.maps{position:absolute;top:458px;left:54px;display:flex;gap:8px}
.map-item{width:144px;font-size:8.5px}
.map-item p{margin-bottom:5px}
.map{height:90px;background:var(--map-fill);color:#fff;display:flex;align-items:center;justify-content:center;font-size:12px}
.map-note{position:absolute;left:720px;top:580px;font-size:8.5px;line-height:1.6}

.ct-label{position:absolute;left:0;top:635px;width:340px;height:54px;background:var(--green);color:#fff;font-family:"M PLUS Rounded 1c",sans-serif;font-weight:800;font-size:34px;padding-left:60px;line-height:54px}
.ct-label span{font-weight:700;font-size:26px;color:var(--ink);position:absolute;left:355px;top:0;white-space:nowrap}
.ct-rule{top:690px}
.water{position:absolute;left:0;right:0;top:700px;height:360px;background:linear-gradient(var(--water-top),var(--water-bottom))}
.ct-photo{position:absolute;left:520px;top:720px;width:260px;height:300px;background:linear-gradient(160deg,#f4f6f7,#d8dde0);border-radius:6px}
.ct-points{position:absolute;left:60px;top:715px;width:440px;list-style:none;font-size:14px;line-height:1.75}
.ct-points li{display:flex;gap:4px;margin-bottom:12px}

.footer{position:absolute;left:0;right:0;top:1060px;bottom:0;background:#fff}
.footer .rule{top:0}
.footer .brand{position:absolute;left:60px;top:30px}
.footer .brand-name{font-size:34px}
.footer .brand-en{position:absolute;left:60px;top:70px}
.address{position:absolute;left:440px;top:40px;font-size:8.5px}
.tel{position:absolute;left:440px;top:58px;display:flex;align-items:center;gap:8px;color:var(--green);font-weight:700;font-size:30px;font-family:"M PLUS Rounded 1c",sans-serif}
.tel-icon{width:30px;height:30px;border-radius:50%;background:var(--green);display:flex;align-items:center;justify-content:center}
</style>
</head>
<body>

<header class="header">
  <div>
    <div class="brand"><span class="brand-dot"></span><span class="brand-name">桜川ファミリー歯科</span></div>
    <div class="brand-en">SAKURAGAWA FAMILY DENTAL CLINIC</div>
  </div>
  <div class="header-sub">からのご案内</div>
</header>
<div class="rule" style="top:96px"></div>

<h1 class="headline">4月 <span class="big">1</span> <span class="dark">日より</span><span class="big">木曜日</span><span class="dark">の診療を開始します。</span></h1>

<section class="sched old">
  <p class="sched-cap">◆今までの診療時間</p>
  <table>
    <tr><th class="time"></th><th>月</th><th>火</th><th>水</th><th>木</th><th>金</th><th>土</th></tr>
    <tr><td class="time">10:00〜13:00</td><td>●</td><td>●</td><td>●</td><td></td><td>●</td><td>●</td></tr>
    <tr><td class="time">14:30〜20:00</td><td>●</td><td>●</td><td>●</td><td></td><td>●</td><td>●</td></tr>
  </table>
  <p class="sched-note">休診日：木曜日・日曜日・祝日</p>
</section>

<svg class="arrow" width="50" height="60" viewBox="0 0 50 60"><polygon points="0,10 28,10 28,0 50,30 28,60 28,50 0,50" fill="var(--green-pale)"/></svg>

<section class="sched nowx">
  <p class="sched-cap">◆4月1日からの診療時間</p>
  <table>
    <tr><th class="time"></th><th>月</th><th>火</th><th>水</th><th>木</th><th>金</th><th>土</th></tr>
    <tr><td class="time">10:00〜13:00</td><td>●</td><td>●</td><td>●</td><td class="new">●</td><td>●</td><td>●</td></tr>
    <tr><td class="time">14:30〜20:00</td><td>●</td><td>●</td><td>●</td><td class="new">●</td><td>●</td><td>●</td></tr>
  </table>
  <p class="sched-note">休診日：日曜日・祝日</p>
</section>

<h2 class="parking-title"><span class="p">P</span>駐車場サービス<small>のご案内</small></h2>
<div class="badge">ご利用<br>ください</div>

<div class="maps">
  <div class="map-item"><p>パークス桜川第1</p><div class="map" role="img" aria-label="パークス桜川第1の地図">map</div></div>
  <div class="map-item"><p>パークス桜川駅前第2</p><div class="map" role="img" aria-label="パークス桜川駅前第2の地図">map</div></div>
  <div class="map-item"><p>パークス桜川三丁目第3</p><div class="map" role="img" aria-label="パークス桜川三丁目第3の地図">map</div></div>
  <div class="map-item"><p>パークス桜川三丁目第4</p><div class="map" role="img" aria-label="パークス桜川三丁目第4の地図">map</div></div>
  <div class="map-item"><p>パークス桜川三丁目第5</p><div class="map" role="img" aria-label="パークス桜川三丁目第5の地図">map</div></div>
</div>
<p class="map-note">※60分無料です<br>※受付にて駐車券提示</p>

<div class="water" role="img" aria-label="水面の波紋の背景写真"></div>
<h2 class="ct-label">歯科用 CT<span>導入しました</span></h2>
<div class="rule ct-rule"></div>
<div class="ct-photo" role="img" aria-label="歯科用CT装置の写真"></div>

<ol class="ct-points">
  <li><span>1)</span><span>レントゲン撮影などでは見えない部分が見え、病状の早期発見に役立ちます。</span></li>
  <li><span>2)</span><span>虫歯や歯周病の進行度が正確に把握でき、患者様に負担の少ない適切な治療に役立ちます。</span></li>
  <li><span>3)</span><span>骨の量や歯根の形などを把握し、歯や神経の場所や状態を正確に把握して、より安全な治療を行えます。</span></li>
  <li><span>4)</span><span>歯や歯茎以外の部分に対しても十分な術前診査が必要な治療（たとえば、インプラント）の「リスク回避」につながります。</span></li>
</ol>

<footer class="footer">
  <div class="rule"></div>
  <div class="brand"><span class="brand-dot"></span><span class="brand-name">桜川ファミリー歯科</span></div>
  <div class="brand-en">SAKURAGAWA FAMILY DENTAL CLINIC</div>
  <p class="address">〒545-0000　大阪府大阪市桜川区桜川町北 1丁目1-8</p>
  <div class="tel">
    <span class="tel-icon"><svg width="18" height="18" viewBox="0 0 24 24"><path fill="#fff" d="M6.6 10.8a15.1 15.1 0 0 0 6.6 6.6l2.2-2.2c.3-.3.7-.4 1-.2 1.1.4 2.3.6 3.6.6.6 0 1 .4 1 1V20c0 .6-.4 1-1 1A17 17 0 0 1 3 4c0-.6.4-1 1-1h3.5c.6 0 1 .4 1 1 0 1.3.2 2.5.6 3.6.1.3 0 .7-.2 1z"/></svg></span>
    06-6000-4182
  </div>
</footer>

</body>
</html>
```